Complete web design based around only our company logo

I need someone to build a web page based around our company logo. I will provide other sites that we like and would want our site to be similar to.
Updates

Please look at these websites to get an idea of our industry

harlow minerals
pel minerals
fenwick royalty
tillamore energy
marlo energy

Our company buys mineral rights, and royalties from mineral owners all over the united states.  We also lease minerals as well. 

What we are trying to have designed is a fully functioning website that you upload to our webhost after we approve of final design.  

Target Market(s)

Oil and Gas/Mineral Owners

Industry/Entity Type

It Company

Font styles to use
Serif
Sans Serif

Colors
9ccb3b

Requirements
Must have
• Quick Contact form

```html
<!DOCTYPE html>
<html lang="en">
<head>
<meta charset="utf-8">
<title>Ridgeline Resources</title>
<link rel="stylesheet" href="https://fonts.googleapis.com/css2?family=Arimo:wght@400;700&family=Bebas+Neue&family=Oswald:wght@300&display=swap">
<style>
:root{
  --green:#3a7d0a;
  --green-text:#3b820c;
  --ink:#1a1a1a;
  --body:#333;
  --muted:#666;
  --panel:#f0f0f0;
  --field-border:#d6d6d6;
  --slate:#666;
  --footer:#000;
  --footer-text:#e6e6e6;
}
*{box-sizing:border-box;margin:0;padding:0}
html,body{width:909px;height:1200px;overflow:hidden}
body{position:relative;background:#fff;font-family:"Arimo",Arial,sans-serif;color:var(--body)}
.abs{position:absolute}

/* header */
.brand{left:90px;top:14px;display:flex;align-items:center;gap:8px}
.brand-mark{width:30px;height:30px;border-radius:50%;background:var(--green)}
.brand-name{font-size:14px;font-weight:700;color:var(--green);line-height:1.05;letter-spacing:.5px;text-transform:uppercase}
.inquiry{right:91px;top:24px;text-align:right}
.inquiry-label{font-size:9px;color:var(--ink)}
.inquiry-phone{font-size:19px;font-weight:700;color:var(--green-text);line-height:1.1}

.green-band{left:0;top:72px;width:909px;height:298px;background:var(--green)}
.main-nav{left:90px;top:72px;width:728px;height:32px;display:flex;justify-content:space-between;align-items:center;padding:0 14px;list-style:none}
.main-nav li{font-size:11px;color:#fff}

.hero-frame{left:89px;top:104px;width:731px;height:293px;background:#fff;box-shadow:0 8px 10px -6px rgba(0,0,0,.35)}
.hero-photo{left:3px;top:4px;width:724px;height:288px;background:linear-gradient(180deg,#9cc3e6 0%,#c9dcea 30%,#8a8274 55%,#a8a39a 80%,#c4c0b8 100%)}

/* intro */
.welcome{left:90px;top:435px;font-size:21px;font-weight:700;color:#000}
.welcome span{font-weight:400;color:var(--green-text)}
.intro{left:90px;top:469px;width:400px;font-size:10.4px;line-height:12.8px;color:var(--body)}
.intro p+p{margin-top:13px}

.feature{top:604px;width:205px}
.feature h2{font-family:"Bebas Neue",sans-serif;font-weight:400;font-size:25px;color:#000;line-height:1;padding-bottom:2px;border-bottom:3px solid var(--green);width:200px}
.feature p{margin-top:12px;font-size:10.4px;line-height:12.8px}

/* testimonials */
.testimonial{left:92px;width:452px;height:90px}
.avatar{left:0;top:0;width:37px;height:49px;border:1px solid #ccc;background:#fff;padding:2px}
.avatar div{width:100%;height:100%;background:linear-gradient(180deg,#8a7a6a,#3c3a3c)}
.bubble{left:52px;top:0;width:400px;height:59px;background:var(--panel);border:1px solid #ddd;padding:11px 36px 11px 10px;font-size:8.4px;line-height:11.2px;color:#555}
.bubble::before{content:"";position:absolute;left:-7px;top:14px;border:6px solid transparent;border-right-color:#ddd;border-left:0}
.person{left:52px;top:70px}
.person-name{font-size:11px;font-weight:700;color:var(--green-text)}
.person-role{font-size:8.6px;color:#555}

/* quick contact */
.quick-contact{left:566px;top:439px;width:253px;height:511px;background:var(--panel)}
.qc-head{left:0;top:0;width:253px;height:44px;background:var(--slate);color:#fff;font-size:10.5px;line-height:13px;padding:9px 18px}
.field{height:24px;background:#fff;border:1px solid var(--field-border);font-size:8.4px;color:#444;padding:7px 11px}
.status{left:16px;top:273px;font-size:8.4px;color:#444}
.radios{left:16px;top:290px;display:flex;gap:8px;font-size:8.4px;color:#999}
.radios span{display:flex;align-items:center;gap:5px}
.radios i{width:10px;height:10px;border:1px solid #ccc;border-radius:50%;background:#fff}
.submit{left:14px;top:468px;width:114px;height:29px;background:var(--slate);color:#fff;font-size:11px;display:flex;align-items:center;gap:14px;padding-left:8px}

/* footer */
.footer{left:0;top:977px;width:909px;height:223px;background:var(--footer);color:var(--footer-text)}
.f-brand{left:90px;top:28px;display:flex;flex-direction:column;align-items:flex-start;gap:8px}
.f-mark{width:50px;height:50px;border-radius:50%;background:#fff;margin-left:26px}
.f-name{font-size:15px;font-weight:700;color:#fff;line-height:1.05;text-transform:uppercase}
.f-about{left:90px;top:127px;width:180px;font-size:8.4px;line-height:10.9px;color:#fff}
.f-heading{font-family:"Bebas Neue",sans-serif;font-size:21px;color:#fff;font-weight:400}
.f-nav{left:364px;top:26px}
.f-links{display:grid;grid-template-columns:104px 100px;margin-top:17px;font-size:10.5px;line-height:13.6px;list-style:none}
.f-contact{left:650px;top:26px}
.f-org{margin-top:17px;font-size:11px;font-weight:700}
.f-addr{margin-top:4px;font-size:8.6px;line-height:13.6px}
.f-phone{margin-top:7px;display:flex;align-items:center;gap:6px;font-family:"Oswald",sans-serif;font-weight:300;font-size:19px}
.f-mail{margin-top:3px;font-size:10.5px}
.f-rule{left:90px;top:187px;width:725px;height:1px;background:#444}
.copyright{left:90px;top:199px;font-size:7.8px;color:#ddd}
.social{left:723px;top:193px;display:flex;gap:5px;list-style:none}
.social li{width:19px;height:19px;border-radius:50%;background:#bbb}
</style>
</head>
<body>

<header>
  <div class="abs brand"><span class="brand-mark"></span><span class="brand-name">Ridgeline<br>Resources</span></div>
  <div class="abs inquiry">
    <div class="inquiry-label">For Inquires Contact Us</div>
    <div class="inquiry-phone">888-555-0147</div>
  </div>
</header>

<div class="abs green-band"></div>
<ul class="abs main-nav">
  <li>Home</li><li>About us</li><li>Active states</li><li>Lease/Purchase minerals</li><li>Testimonials</li><li>Careers</li><li>Contact us</li>
</ul>

<div class="abs hero-frame">
  <div class="abs hero-photo" role="img" aria-label="Open-pit mine with a yellow excavator loading a dump truck under a blue sky"></div>
</div>

<main>
  <h1 class="abs welcome">Welcome to <span>Ridgeline Resources, LLC</span></h1>
  <div class="abs intro">
    <p>Lorem ipsum dolor sit amet, consectetuer adipiscing elit, sed diam nonummy nibh euismod tincidunt ut laoreet dolore magna aliquam erat volutpat. Ut wisi enim ad minim veniam, quis nostrud exerci tation ullamcorper suscipit lobortis nisl ut aliquip ex ea commodo consequat.</p>
    <p>Duis autem vel eum iriure dolor in hendrerit in vulputate velit esse molestie consequat, vel illum dolore eu feugiat nulla facilisis at vero eros et accumsan et iusto odio dignissim qui blandit praesent luptatum zzril delenit augue duis dolore te feugait nulla facilisi.</p>
  </div>

  <section class="abs feature" style="left:90px">
    <h2>What we do</h2>
    <p>Lorem ipsum dolor sit amet, consectetuer adipiscing elit, sed diam nonummy nibh euismod tincidunt ut laoreet dolore magna aliquam erat volutpat. Ut wisi enim ad minim veniam, quis nostrud exerci tation ullamcorper suscipit lobortis nisl ut aliquip ex ea commodo consequat.</p>
  </section>
  <section class="abs feature" style="left:337px">
    <h2>How we do it</h2>
    <p>Duis autem vel eum iriure dolor in hendrerit in vulputate velit esse molestie consequat, vel illum dolore eu feugiat nulla facilisis at vero eros et accumsan et iusto odio dignissim qui blandit praesent luptatum zzril delenit augue duis dolore te feugait ulla facilisi.</p>
  </section>

  <article class="abs testimonial" style="top:758px">
    <div class="abs avatar"><div role="img" aria-label="Portrait of Tom Ellery"></div></div>
    <blockquote class="abs bubble">Ut enim ad minim veniam, quis nostrud exercitation ullamco laboris nisi ut aliquip ex ea commodo consequat. Duis aute irure dolor in reprehenderit in voluptate velit esse cillum praesent luptatum zzril delenit augue duis dolore te feugait ulla facilisi.</blockquote>
    <div class="abs person"><div class="person-name">Tom Ellery</div><div class="person-role">Real Estate Guru</div></div>
  </article>
  <article class="abs testimonial" style="top:866px">
    <div class="abs avatar"><div role="img" aria-label="Portrait of Mark Dorsey"></div></div>
    <blockquote class="abs bubble">Ut enim ad minim veniam, quis nostrud exercitation ullamco laboris nisi ut aliquip ex ea commodo consequat. Duis aute irure dolor in reprehenderit in voluptate velit esse cillum praesent luptatum zzril delenit augue duis dolore te feugait ulla facilisi.</blockquote>
    <div class="abs person"><div class="person-name">Mark Dorsey</div><div class="person-role">Expert Miner</div></div>
  </article>

  <form class="abs quick-contact">
    <div class="abs qc-head">Contact Wade today for details about a lease or purchase offering for your property</div>
    <div class="abs field" style="left:13px;top:56px;width:228px">Name *</div>
    <div class="abs field" style="left:13px;top:86px;width:228px">Address *</div>
    <div class="abs field" style="left:13px;top:116px;width:113px">Country *</div>
    <div class="abs field" style="left:127px;top:116px;width:114px">State *</div>
    <div class="abs field" style="left:13px;top:146px;width:113px">City *</div>
    <div class="abs field" style="left:127px;top:146px;width:114px">Zip *</div>
    <div class="abs field" style="left:13px;top:176px;width:228px">Phone *</div>
    <div class="abs field" style="left:13px;top:206px;width:228px">Email *</div>
    <div class="abs field" style="left:13px;top:236px;width:228px">Total Acres *</div>
    <div class="abs status">Current status of mineral rights</div>
    <div class="abs radios"><span><i></i>for sale</span><span><i></i>for lease</span></div>
    <div class="abs field" style="left:13px;top:313px;width:228px;height:141px">Message *</div>
    <div class="abs submit">
      <svg width="19" height="19" viewBox="0 0 20 20"><circle cx="10" cy="10" r="10" fill="#fff"/><path d="M5 10h9M10 6l4 4-4 4" stroke="#666" stroke-width="2.4" fill="none"/></svg>
      SUBMIT
    </div>
  </form>
</main>

<footer class="abs footer">
  <div class="abs f-brand"><span class="f-mark"></span><span class="f-name">Ridgeline<br>Resources</span></div>
  <p class="abs f-about">Lorem ipsum dolor sit amet, consectetuer adipiscing elit, sed diam nonummy nibh euismod tincidunt ut laoreet dolore magna aliquam erat volutpat.</p>

  <nav class="abs f-nav">
    <h3 class="f-heading">Navigation</h3>
    <ul class="f-links">
      <li>Home</li><li>Careers</li>
      <li>About us</li><li>Contact us</li>
      <li>Active states</li><li>Terms of Use</li>
      <li>Lease/purchase minerals</li><li>Privacy Policy</li>
    </ul>
  </nav>

  <div class="abs f-contact">
    <h3 class="f-heading">Contact us</h3>
    <div class="f-org">Ridgeline Resources</div>
    <div class="f-addr">4410 Larch Avenue Suite 218<br>Bellmont, New York 556410</div>
    <div class="f-phone">
      <svg width="20" height="20" viewBox="0 0 20 20"><circle cx="10" cy="10" r="9" fill="none" stroke="#ddd" stroke-width="1.3"/><path d="M7 5l2 2.5-1.2 1.3c.7 1.5 1.9 2.7 3.4 3.4l1.3-1.2L15 13l-1.4 1.6C10 14.3 5.7 10 5.4 6.4z" fill="#ddd"/></svg>
      0-12-5550198
    </div>
    <div class="f-mail">info@ridgelineresources</div>
  </div>

  <div class="abs f-rule"></div>
  <p class="abs copyright">© Copyright 2014 Ridgeline Resources. All Rights Reserved</p>
  <ul class="abs social" aria-label="Social links"><li></li><li></li><li></li><li></li></ul>
</footer>

</body>
</html>
```